Frostbell Hollow LV, A Magical Holiday Festival

frostbellhollowlv-example.com
Need to include the following:
Dates: Dec 14- Dec 30
kids 48'' and under free, presale tickets $6, wonder pass $25(17 days pass) website: frostbellhollowlv-example.com, ice skating rink, snow park, santa house, first 1000 kids will receive a gift from Santa on Christmas day.
Location: Copperpine Casino, 4172 Maple Fern Road.
Also need to include RQN logo and Grand Plains Supper Fair logo (I attached)

Industry/Entity Type

Festival

Font styles to use
Decorative

Requirements
Must have
• Date : December 14- December 30
• Location: Copperpine Casino
Nice to have
• Santa House, christmas lights, ice skating rink, snow park

```html
<!DOCTYPE html>
<html lang="en">
<head>
<meta charset="utf-8">
<title>Frostbell Hollow LV – A Magical Holiday Festival</title>
<link href="https://fonts.googleapis.com/css2?family=Berkshire+Swash&family=Mountains+of+Christmas:wght@700&family=Sniglet:wght@800&family=Libre+Caslon+Text:wght@700&family=Archivo:wght@800&display=swap" rel="stylesheet">
<style>
  :root {
    --sky-top: #c9ecf8;
    --sky-mid: #2a8fd0;
    --sky-deep: #1a3fa0;
    --night: #0f2a6e;
    --snow: #ffffff;
    --title-blue: #2a3a9c;
    --navy: #1f2d6b;
    --crimson: #a8232a;
    --badge-white: #ffffff;
  }
  html, body {
    margin: 0;
    padding: 0;
    overflow: hidden;
    background: #eef3f8;
  }
  .poster {
    position: relative;
    width: 848px;
    height: 1200px;
    overflow: hidden;
    color: var(--snow);
  }
  .winter-scene {
    position: absolute;
    inset: 0;
    background:
      radial-gradient(ellipse 60% 40% at 50% 30%, #3aa6e0 0%, transparent 70%),
      linear-gradient(180deg, var(--sky-top) 0%, #5ec0ea 14%, var(--sky-mid) 36%, var(--sky-deep) 62%, var(--night) 80%, #3e5f9c 100%);
  }
  .festival-name {
    position: absolute;
    top: 112px;
    left: 0;
    width: 100%;
    margin: 0;
    text-align: center;
    font-family: "Berkshire Swash", "Mountains of Christmas", cursive;
    font-weight: 400;
    color: var(--title-blue);
    font-size: 68px;
    line-height: 72px;
    text-shadow: 0 0 6px rgba(255,255,255,0.9), 0 0 2px #fff;
  }
  .festival-tagline {
    position: absolute;
    top: 264px;
    left: 0;
    width: 100%;
    text-align: center;
    font-family: "Libre Caslon Text", serif;
    font-weight: 700;
    font-size: 15px;
    letter-spacing: 0.5px;
    color: var(--title-blue);
    text-transform: uppercase;
    text-shadow: 0 0 3px #fff;
  }
  .festival-dates {
    position: absolute;
    top: 318px;
    left: 0;
    width: 100%;
    text-align: center;
    font-family: "Mountains of Christmas", "Berkshire Swash", cursive;
    font-weight: 700;
    font-size: 50px;
    line-height: 1;
  }
  .festival-location {
    position: absolute;
    top: 389px;
    left: 0;
    width: 100%;
    text-align: center;
    font-family: "Libre Caslon Text", serif;
    font-weight: 700;
    font-size: 17px;
    text-transform: uppercase;
  }
  .attractions {
    position: absolute;
    top: 444px;
    left: 0;
    width: 100%;
    margin: 0;
    padding: 0;
    list-style: none;
    text-align: center;
    font-family: "Sniglet", sans-serif;
    font-weight: 800;
    font-size: 48px;
    line-height: 56px;
    text-transform: uppercase;
    letter-spacing: 1px;
  }
  .gift-note {
    position: absolute;
    top: 636px;
    left: 0;
    width: 100%;
    margin: 0;
    text-align: center;
    font-family: "Libre Caslon Text", serif;
    font-weight: 700;
    font-size: 19px;
  }
  .badge {
    position: absolute;
    border-radius: 50%;
    display: flex;
    flex-direction: column;
    align-items: center;
    justify-content: center;
    text-align: center;
    font-family: "Archivo", sans-serif;
    font-weight: 800;
    text-transform: uppercase;
    box-sizing: border-box;
  }
  .badge-partners {
    left: 88px; top: 828px; width: 232px; height: 232px;
    background: var(--badge-white);
    color: var(--navy);
    justify-content: flex-end;
    padding-bottom: 40px;
    gap: 14px;
  }
  .partner-name {
    font-size: 17px;
    color: var(--navy);
    line-height: 1.1;
  }
  .badge-tickets {
    left: 102px; top: 670px; width: 196px; height: 196px;
    background: var(--navy);
    border: 3px solid var(--badge-white);
  }
  .badge-tickets .label { font-size: 12px; }
  .badge-tickets .value-sm { font-size: 19px; margin: 4px 0 14px; }
  .badge-tickets .value { font-size: 28px; margin-top: 2px; }
  .badge-pass {
    left: 256px; top: 772px; width: 188px; height: 188px;
    background: var(--crimson);
    border: 3px solid var(--badge-white);
  }
  .badge-pass .label { font-size: 14px; }
  .badge-pass .value { font-size: 28px; margin: 4px 0 2px; }
  .badge-pass .note { font-size: 13px; }
  .santa-figure {
    position: absolute;
    left: 566px; top: 672px; width: 236px; height: 450px;
    border-radius: 110px 110px 40px 40px;
    background: linear-gradient(180deg, #f3f0ea 0%, #d6232c 35%, #b81c24 70%, #1a1a1a 100%);
    opacity: 0.9;
  }
  .website {
    position: absolute;
    top: 1132px;
    left: 0;
    width: 100%;
    text-align: center;
    font-family: "Libre Caslon Text", serif;
    font-weight: 700;
    font-size: 24px;
    text-transform: uppercase;
  }
</style>
</head>
<body>
<main class="poster">
  <div class="winter-scene" role="img" aria-label="Starry frosted blue sky fading to a snowy night landscape with pine forest and a lit cabin"></div>

  <h1 class="festival-name">Frostbell<br>Hollow</h1>
  <div class="festival-tagline">A Magical Holiday Festival</div>

  <div class="festival-dates">Dec 14–Dec 30</div>
  <div class="festival-location">Location: Copperpine Casino, 4172 Maple Fern Road</div>

  <ul class="attractions">
    <li>Ice Skating Rink</li>
    <li>Snow Park</li>
    <li>Santa House</li>
  </ul>

  <p class="gift-note">First 1000 kids will receive a gift from Santa on Christmas day.</p>

  <div class="badge badge-partners">
    <span class="partner-name">RQN</span>
    <span class="partner-name">Grand Plains<br>Supper Fair</span>
  </div>

  <div class="badge badge-tickets">
    <span class="label">Kids 48" and under</span>
    <span class="value-sm">Free</span>
    <span class="label">Presale tickets</span>
    <span class="value">$6</span>
  </div>

  <div class="badge badge-pass">
    <span class="label">Wonder Pass</span>
    <span class="value">$25</span>
    <span class="note">(17 days pass)</span>
  </div>

  <div class="santa-figure" role="img" aria-label="Illustrated Santa Claus in red suit waving"></div>

  <div class="website">frostbellhollowlv-example.com</div>
</main>
</body>
</html>
```